Advertisement for tellmark Ad

We are looking to copy a mailer style design that would normally be sent out to a mailbox. However we have decided to simply use it and run an add on Tellmark. please check photo sizes for tellmark to make sure your design will work.

also please try to use the colors from our website: riverbendhollow@mailnest.com

we want the same layout as the ad we sent in the files, with different photos and color scheme.

Target Market(s)

dog owners with busy schedules

Font styles to use
Sans Serif

Colors

Designer to choose only greyscale colors for use in the design.

```html
<!DOCTYPE html>
<html lang="en">
<head>
<meta charset="utf-8">
<title>Riverbend Hollow Canine Center – Daycare Offer</title>
<link href="https://fonts.googleapis.com/css2?family=Righteous&family=Montserrat:wght@600;700&display=swap" rel="stylesheet">
<style>
  :root {
    --panel-dark: #3a3a3a;
    --panel-light: #8a8a8a;
    --accent: #d4d4d4;
    --black: #000000;
    --white: #ffffff;
    --photo-light: #c4c4c4;
    --photo-mid: #8f8f8f;
    --photo-dark: #4e4e4e;
  }
  * { margin: 0; padding: 0; box-sizing: border-box; }
  html, body { width: 1200px; height: 628px; overflow: hidden; background: var(--white); }
  .ad {
    position: relative;
    width: 1200px;
    height: 628px;
    overflow: hidden;
    font-family: "Montserrat", sans-serif;
    color: var(--white);
  }
  .hero-photo {
    position: absolute;
    left: 0; top: 0;
    width: 560px; height: 425px;
    background: linear-gradient(160deg, var(--photo-light) 0%, var(--photo-mid) 55%, var(--photo-dark) 100%);
  }
  .brand-mark {
    position: absolute;
    left: 14px; top: 390px;
    display: flex; align-items: center; gap: 8px;
    font-weight: 700;
    font-size: 15px;
    letter-spacing: 1px;
    color: var(--white);
    text-transform: uppercase;
  }
  .brand-mark .dot {
    width: 12px; height: 12px;
    background: var(--white);
  }
  .info-panel {
    position: absolute;
    left: 0; top: 0;
    width: 1200px; height: 425px;
    background: linear-gradient(90deg, var(--panel-dark) 40%, var(--panel-light) 100%);
    clip-path: polygon(490px 0, 1200px 0, 1200px 425px, 535px 425px);
  }
  .headline {
    position: absolute;
    left: 578px; top: 34px;
    font-family: "Righteous", sans-serif;
    font-size: 58px;
    line-height: 52px;
    font-weight: 400;
    text-transform: uppercase;
  }
  .features {
    position: absolute;
    left: 578px; top: 168px;
    font-weight: 700;
    font-size: 20.5px;
    line-height: 27px;
    text-transform: uppercase;
  }
  .features p + p { margin-top: 26px; }
  .divider {
    position: absolute;
    left: 578px; top: 313px;
    width: 548px; height: 1px;
    background: rgba(255,255,255,0.7);
  }
  .contact {
    position: absolute;
    left: 578px; top: 333px;
    font-style: normal;
    font-weight: 700;
    font-size: 17.5px;
    line-height: 26px;
  }
  .offers {
    position: absolute;
    left: 0; top: 425px;
    width: 1200px; height: 203px;
    background: var(--black);
    display: flex;
  }
  .offer {
    flex: 1;
    position: relative;
    text-align: center;
    padding-top: 16px;
  }
  .offer + .offer::before {
    content: "";
    position: absolute;
    left: 0; top: 34px;
    height: 140px;
    border-left: 6px dotted var(--white);
  }
  .offer-title {
    font-family: "Righteous", sans-serif;
    font-size: 42px;
    line-height: 48px;
    font-weight: 400;
    color: var(--accent);
    text-transform: uppercase;
    height: 110px;
    display: flex; align-items: center; justify-content: center;
  }
  .offer-terms {
    margin-top: 8px;
    font-weight: 600;
    font-size: 13px;
    line-height: 17px;
  }
</style>
</head>
<body>
  <main class="ad">
    <div class="hero-photo" role="img" aria-label="Photo of four happy dogs playing on a wooden deck in front of a wooden fence"></div>
    <div class="brand-mark"><span class="dot"></span>Riverbend Hollow</div>

    <section class="info-panel">
      <h1 class="headline">Not your typical<br>dog daycare</h1>
      <div class="features">
        <p>Safe,open play daycare<br>exercise &amp; education</p>
        <p>Fun filled days with their BFFF<br>(best furry friend forever)</p>
      </div>
      <div class="divider"></div>
      <address class="contact">
        Riverbend Hollow Canine Center<br>
        418 North Birch Avenue Maple Falls IA<br>
        555-013-0187
      </address>
    </section>

    <section class="offers">
      <div class="offer">
        <h2 class="offer-title">Free first day<br>of daycare!*</h2>
        <p class="offer-terms">*Advanced reservations required.<br>CALL to schedule your appointment.<br>valid until 8/31/20</p>
      </div>
      <div class="offer">
        <h2 class="offer-title">One free<br>bath!*</h2>
        <p class="offer-terms">*Advanced reservations required.<br>CALL to schedule your appointment.<br>valid until 8/31/20</p>
      </div>
      <div class="offer">
        <h2 class="offer-title">$ 20 off<br>first groom</h2>
        <p class="offer-terms">*Advanced reservations required.<br>CALL to schedule your appointment.<br>valid until 8/31/20</p>
      </div>
    </section>
  </main>
</body>
</html>
```